Realtor branding business card

modern, simple and self branding. Broker office logo needs to be used but not emphasized. Looking to brand myself

Target Market(s)

buyers, sellers and investors

Industry/Entity Type

Realtor

Contact Information for Business Card

Sample of my current business card on file

Requirements
Must have
• my website - emilioverdaskt.com
• Realtor logo
• Fair housing logo
Nice to have
• Colors from office logo but not a must
Should not have
• Do not want headshot

```html
<!DOCTYPE html>
<html lang="en">
<head>
<meta charset="utf-8">
<title>Brightpath Realty Group – Business Cards</title>
<link rel="stylesheet" href="https://fonts.googleapis.com/css2?family=Arimo:wght@400;700&display=swap">
<style>
  :root {
    --purple: #2e1c7c;
    --purple-deep: #24156a;
    --red: #e1301f;
    --white: #ffffff;
    --paper: #f7f7f9;
    --stage: #e9e9ec;
    --ink-soft: #3a2d86;
  }
  * { box-sizing: border-box; margin: 0; padding: 0; }
  html, body {
    width: 1200px; height: 997px; overflow: hidden;
    background: var(--stage);
    font-family: "Arimo", Arial, sans-serif;
  }
  .card {
    position: absolute;
    width: 560px; height: 320px;
    background: var(--paper);
    box-shadow: 0 10px 28px rgba(0,0,0,.18);
    overflow: hidden;
  }
  .card--front { left: 60px; top: 150px; }
  .card--back  { left: 580px; top: 520px; }

  .brand {
    position: absolute;
    display: flex; align-items: center; gap: 14px;
    color: var(--purple);
    font-weight: 700;
    line-height: .95;
    white-space: nowrap;
  }
  .brand__dot {
    width: 26px; height: 26px; border-radius: 50%;
    background: var(--red); flex: none;
  }
  .brand__name { display: block; }
  .brand__name small { display: block; font-size: .55em; }

  .card--front .brand { left: 44px; top: 62px; font-size: 56px; }
  .card--front .band {
    position: absolute; left: 0; right: 0; top: 196px; height: 62px;
    background: var(--purple);
    border-top: 3px solid var(--red);
    border-bottom: 3px solid var(--red);
    display: flex; align-items: center; justify-content: flex-end;
    padding-right: 40px;
  }
  .website {
    color: var(--white); font-weight: 700; font-size: 17px; letter-spacing: 2px;
  }
  .tagline {
    position: absolute; right: 40px; top: 276px;
    color: var(--ink-soft); font-size: 12px; letter-spacing: .6px;
    white-space: nowrap;
  }

  .card--back .brand { left: 150px; top: 26px; font-size: 44px; }
  .card--back .band {
    position: absolute; left: 0; right: 0; top: 142px; height: 118px;
    background: var(--purple);
    border-top: 3px solid var(--red);
    border-bottom: 3px solid var(--red);
    display: flex; align-items: center;
  }
  .agent { width: 250px; padding-left: 40px; text-align: right; padding-right: 24px; }
  .agent__name { color: var(--red); font-weight: 700; font-size: 18px; letter-spacing: .5px; white-space: nowrap; }
  .agent__title { color: var(--white); font-size: 15px; margin-top: 2px; }
  .divider { width: 1px; height: 66px; background: var(--red); }
  .contact { list-style: none; padding-left: 26px; }
  .contact li {
    display: flex; align-items: center; gap: 10px;
    color: var(--white); font-size: 14px; line-height: 24px;
    white-space: nowrap;
  }
  .contact svg { width: 16px; height: 16px; flex: none; }
  .housing-badge {
    position: absolute; right: 26px; top: 104px;
    width: 26px; height: 26px; background: var(--purple-deep);
  }
  .address {
    position: absolute; left: 0; right: 0; top: 276px;
    text-align: center; color: var(--purple); font-weight: 700; font-size: 15px;
    white-space: nowrap;
  }
</style>
</head>
<body>

<section class="card card--front">
  <div class="brand">
    <span class="brand__dot"></span>
    <span class="brand__name">Brightpath<small>Realty Group</small></span>
  </div>
  <div class="band"><span class="website">www.emilioverdaskt.com</span></div>
  <p class="tagline">GUIDING EVERY MOVE TOWARDS A CONFIDENT CLOSING.</p>
</section>

<section class="card card--back">
  <div class="brand">
    <span class="brand__dot"></span>
    <span class="brand__name">Brightpath<small>Realty Group</small></span>
  </div>
  <span class="housing-badge" role="img" aria-label="Fair housing badge"></span>
  <div class="band">
    <div class="agent">
      <p class="agent__name">EMILIO VERDAS, PA</p>
      <p class="agent__title">Realtor</p>
    </div>
    <span class="divider"></span>
    <ul class="contact">
      <li>
        <svg viewBox="0 0 16 16" aria-hidden="true"><circle cx="8" cy="8" r="8" fill="#e1301f"/><path d="M5 4.5h2l.6 2-1 .8a5 5 0 0 0 2.1 2.1l.8-1 2 .6v2a1 1 0 0 1-1 1A6.5 6.5 0 0 1 4 5.5a1 1 0 0 1 1-1z" fill="#fff"/></svg>
        (555) 218-4470
      </li>
      <li>
        <svg viewBox="0 0 16 16" aria-hidden="true"><circle cx="8" cy="8" r="8" fill="#e1301f"/><path d="M5 4.5h2l.6 2-1 .8a5 5 0 0 0 2.1 2.1l.8-1 2 .6v2a1 1 0 0 1-1 1A6.5 6.5 0 0 1 4 5.5a1 1 0 0 1 1-1z" fill="#fff"/></svg>
        (555) 630-1900
      </li>
      <li>
        <svg viewBox="0 0 16 16" aria-hidden="true"><circle cx="8" cy="8" r="8" fill="#e1301f"/><rect x="4" y="5.5" width="8" height="5.5" fill="#fff"/><path d="M4 5.5l4 3 4-3" fill="none" stroke="#e1301f" stroke-width=".9"/></svg>
        verdasrealty@mailbox.com
      </li>
    </ul>
  </div>
  <p class="address">48 Lakeview Parkway #310, Cedar Springs FL 30412</p>
</section>

</body>
</html>
```